Design für 3-Monatskalender
Zielgruppe
Hallo, wir benötigen ein Design bzw. fertige Druckdaten für einen 3 Monatskalender mit den Feiertagen aus DE, AT und CH.
Format ist DIN A6, der Kalender wird benötigt für das Jahr 2024 und 2025.
Aufgabenstellung
Format: DIN A6
Kalendarium 2024 und 2025
Feiertage aus DE, AT und CH
Beispiel anbei, wichtig ist, das wir einen Magnetischen Ring als Datumsschieber nehmen. Der Ring hat die Maße: Durchmesser = 12mm Innendruchmesser = 10mm

```html
<!DOCTYPE html>
<html lang="de">
<head>
<meta charset="utf-8">
<title>3-Monatskalender 2024/2025</title>
<link rel="stylesheet" href="https://fonts.googleapis.com/css2?family=Lora:ital,wght@0,400;0,500;0,600;1,400&display=swap">
<style>
  :root{
    --page:#ffffff;
    --sunday:#e0197d;
    --ring:#e0197d;
    --ink:#2e3852;
    --label:#5a5f6b;
  }
  .theme-gold{
    --side:#050505;
    --band:#e6bf22;
    --accent:#e6bf22;
    --title:#111111;
    --digit:#2e3852;
  }
  .theme-slate{
    --side:#475269;
    --band:#a3cbd1;
    --accent:#f07a73;
    --title:#f07a73;
    --digit:#3d4862;
  }
  *{box-sizing:border-box;margin:0;padding:0}
  html,body{width:1200px;height:826px;overflow:hidden;background:var(--page)}
  body{position:relative;font-family:"Lora",serif;color:var(--ink)}

  .calendar{
    position:absolute;top:35px;width:537px;height:757px;background:#fff;
    box-shadow:3px 3px 6px rgba(0,0,0,.35);overflow:hidden;
  }
  .calendar.left{left:46px}
  .calendar.right{left:618px}
  .sidebar{position:absolute;left:0;top:0;width:98px;height:100%;background:var(--side)}

  .month{position:absolute;left:0;width:100%}
  .month .year{
    position:absolute;left:20px;top:-1px;font-size:20px;letter-spacing:3.4px;
    color:var(--accent);font-weight:400;
  }
  .month .week-label{
    position:absolute;right:calc(537px - 73px);top:20px;text-align:right;
    font-size:6.6px;line-height:8px;color:#fff;
  }
  .month .title{
    position:absolute;right:44px;top:1px;font-size:11.5px;letter-spacing:2.6px;
    color:var(--title);font-weight:500;
  }
  .weekdays{
    position:absolute;left:122px;top:20px;display:grid;grid-template-columns:repeat(7,56px);
  }
  .weekdays span{
    text-align:center;font-size:6.6px;line-height:8px;font-style:italic;color:var(--label);
  }
  .band{position:absolute;left:0;width:100%}
  .row{display:grid;grid-template-columns:98px 1fr;height:27.4px}
  .week{
    text-align:right;padding-right:24px;color:#fff;font-size:16px;font-weight:500;line-height:27.4px;
  }
  .days{
    display:grid;grid-template-columns:24px repeat(7,56px);background:var(--band);
    border-bottom:1px solid rgba(255,255,255,.45);
  }
  .days span{
    text-align:center;font-size:18px;font-weight:500;line-height:27px;color:var(--digit);
    letter-spacing:-.3px;
  }
  .days span:first-child{grid-column:2}
  .days .sun{color:var(--sunday)}
  .slider-ring{
    position:absolute;left:296px;top:43px;width:52px;height:52px;border-radius:50%;
    border:4.4px solid var(--ring);
  }

  .holiday-label{
    position:absolute;right:calc(537px - 79px);top:690px;text-align:right;
    font-size:7.2px;line-height:11.4px;font-style:italic;color:var(--accent);
  }
  .holidays{
    position:absolute;top:691px;display:grid;font-size:7.2px;line-height:8.1px;
  }
  .holidays .name{text-align:right;padding-right:3px;color:#222}
  .holidays .date{
    border-left:1px solid var(--accent);padding-left:4px;font-style:italic;color:var(--accent);
  }
  .holidays.de{left:110px;grid-template-columns:125px 50px}
  .holidays.en{left:222px;grid-template-columns:140px 80px}
  .holidays.fr{left:400px;grid-template-columns:75px 50px}
</style>
</head>
<body>

<!-- ========== Variante Gold ========== -->
<div class="calendar left theme-gold">
  <div class="sidebar"></div>

  <section class="month" style="top:21px">
    <div class="year">2024</div>
    <div class="week-label">Woche<br>Week<br>Semaine</div>
    <div class="title">DEZEMBER . DECEMBER . DÉCEMBRE</div>
    <div class="weekdays">
      <span>Montag<br>Monday<br>Lundi</span><span>Dienstag<br>Tuesday<br>Mardi</span><span>Mittwoch<br>Wednesday<br>Mercredi</span><span>Donnerstag<br>Thursday<br>Jeudi</span><span>Freitag<br>Friday<br>Vendredi</span><span>Samstag<br>Saturday<br>Samedi</span><span>Sonntag<br>Sunday<br>Dimanche</span>
    </div>
    <div class="band" style="top:55px">
      <div class="row"><div class="week">48</div><div class="days"><span></span><span></span><span></span><span></span><span></span><span></span><span class="sun">1</span></div></div>
      <div class="row"><div class="week">49</div><div class="days"><span>2</span><span>3</span><span>4</span><span>5</span><span>6</span><span>7</span><span class="sun">8</span></div></div>
      <div class="row"><div class="week">50</div><div class="days"><span>9</span><span>10</span><span>11</span><span>12</span><span>13</span><span>14</span><span class="sun">15</span></div></div>
      <div class="row"><div class="week">51</div><div class="days"><span>16</span><span>17</span><span>18</span><span>19</span><span>20</span><span>21</span><span class="sun">22</span></div></div>
      <div class="row"><div class="week">52</div><div class="days"><span>23</span><span>24</span><span>25</span><span>26</span><span>27</span><span>28</span><span class="sun">29</span></div></div>
      <div class="row"><div class="week">53</div><div class="days"><span>30</span><span>31</span><span></span><span></span><span></span><span></span><span></span></div></div>
      <div class="slider-ring"></div>
    </div>
  </section>

  <section class="month" style="top:265px">
    <div class="year">2025</div>
    <div class="week-label">Woche<br>Week<br>Semaine</div>
    <div class="title">JANUAR . JANUARY . JANVIER</div>
    <div class="weekdays">
      <span>Montag<br>Monday<br>Lundi</span><span>Dienstag<br>Tuesday<br>Mardi</span><span>Mittwoch<br>Wednesday<br>Mercredi</span><span>Donnerstag<br>Thursday<br>Jeudi</span><span>Freitag<br>Friday<br>Vendredi</span><span>Samstag<br>Saturday<br>Samedi</span><span>Sonntag<br>Sunday<br>Dimanche</span>
    </div>
    <div class="band" style="top:57px">
      <div class="row"><div class="week">1</div><div class="days"><span></span><span></span><span>1</span><span>2</span><span>3</span><span>4</span><span class="sun">5</span></div></div>
      <div class="row"><div class="week">2</div><div class="days"><span>6</span><span>7</span><span>8</span><span>9</span><span>10</span><span>11</span><span class="sun">12</span></div></div>
      <div class="row"><div class="week">3</div><div class="days"><span>13</span><span>14</span><span>15</span><span>16</span><span>17</span><span>18</span><span class="sun">19</span></div></div>
      <div class="row"><div class="week">4</div><div class="days"><span>20</span><span>21</span><span>22</span><span>23</span><span>24</span><span>25</span><span class="sun">26</span></div></div>
      <div class="row"><div class="week">5</div><div class="days"><span>27</span><span>28</span><span>29</span><span>30</span><span>31</span><span></span><span></span></div></div>
    </div>
  </section>

  <section class="month" style="top:484px">
    <div class="year">2025</div>
    <div class="week-label">Woche<br>Week<br>Semaine</div>
    <div class="title">FEBRUAR . FEBRUARY . FÉVRIER</div>
    <div class="weekdays">
      <span>Montag<br>Monday<br>Lundi</span><span>Dienstag<br>Tuesday<br>Mardi</span><span>Mittwoch<br>Wednesday<br>Mercredi</span><span>Donnerstag<br>Thursday<br>Jeudi</span><span>Freitag<br>Friday<br>Vendredi</span><span>Samstag<br>Saturday<br>Samedi</span><span>Sonntag<br>Sunday<br>Dimanche</span>
    </div>
    <div class="band" style="top:55px">
      <div class="row"><div class="week">5</div><div class="days"><span></span><span></span><span></span><span></span><span></span><span>1</span><span class="sun">2</span></div></div>
      <div class="row"><div class="week">6</div><div class="days"><span>3</span><span>4</span><span>5</span><span>6</span><span>7</span><span>8</span><span class="sun">9</span></div></div>
      <div class="row"><div class="week">7</div><div class="days"><span>10</span><span>11</span><span>12</span><span>13</span><span>14</span><span>15</span><span class="sun">16</span></div></div>
      <div class="row"><div class="week">8</div><div class="days"><span>17</span><span>18</span><span>19</span><span>20</span><span>21</span><span>22</span><span class="sun">23</span></div></div>
      <div class="row"><div class="week">9</div><div class="days"><span>24</span><span>25</span><span>26</span><span>27</span><span>28</span><span></span><span></span></div></div>
    </div>
  </section>

  <div class="holiday-label">Feiertage<br>Holidays<br>Jours fériés</div>
  <div class="holidays de">
    <span class="name">Neujahrstag</span><span class="date">Jan 01</span>
    <span class="name">Offenbarung (BW, BY &amp; ST)</span><span class="date">Jan 06</span>
    <span class="name">Weihnachtsfeiertag</span><span class="date">Dez 25</span>
    <span class="name">Weihnachtsfeiertage</span><span class="date">Dez 26</span>
  </div>
  <div class="holidays en">
    <span class="name">New Year's Day</span><span class="date">01 January</span>
    <span class="name">Epiphany</span><span class="date">06 January</span>
    <span class="name">Immaculate Conception</span><span class="date">08 December</span>
    <span class="name">Christmas Eve</span><span class="date">24 December</span>
    <span class="name">Christmas Day</span><span class="date">25 December</span>
    <span class="name">Boxing Day</span><span class="date">26 December</span>
    <span class="name">New Year</span><span class="date">31 December</span>
  </div>
  <div class="holidays fr">
    <span class="name">Jour de l'An</span><span class="date">janv-01</span>
    <span class="name">Noël</span><span class="date">déc-25</span>
    <span class="name">Saint-Étienne</span><span class="date">déc-26</span>
  </div>
</div>

<!-- ========== Variante Schiefer ========== -->
<div class="calendar right theme-slate">
  <div class="sidebar"></div>

  <section class="month" style="top:21px">
    <div class="year">2024</div>
    <div class="week-label">Woche<br>Week<br>Semaine</div>
    <div class="title">DEZEMBER . DECEMBER . DÉCEMBRE</div>
    <div class="weekdays">
      <span>Montag<br>Monday<br>Lundi</span><span>Dienstag<br>Tuesday<br>Mardi</span><span>Mittwoch<br>Wednesday<br>Mercredi</span><span>Donnerstag<br>Thursday<br>Jeudi</span><span>Freitag<br>Friday<br>Vendredi</span><span>Samstag<br>Saturday<br>Samedi</span><span>Sonntag<br>Sunday<br>Dimanche</span>
    </div>
    <div class="band" style="top:55px">
      <div class="row"><div class="week">48</div><div class="days"><span></span><span></span><span></span><span></span><span></span><span></span><span class="sun">1</span></div></div>
      <div class="row"><div class="week">49</div><div class="days"><span>2</span><span>3</span><span>4</span><span>5</span><span>6</span><span>7</span><span class="sun">8</span></div></div>
      <div class="row"><div class="week">50</div><div class="days"><span>9</span><span>10</span><span>11</span><span>12</span><span>13</span><span>14</span><span class="sun">15</span></div></div>
      <div class="row"><div class="week">51</div><div class="days"><span>16</span><span>17</span><span>18</span><span>19</span><span>20</span><span>21</span><span class="sun">22</span></div></div>
      <div class="row"><div class="week">52</div><div class="days"><span>23</span><span>24</span><span>25</span><span>26</span><span>27</span><span>28</span><span class="sun">29</span></div></div>
      <div class="row"><div class="week">53</div><div class="days"><span>30</span><span>31</span><span></span><span></span><span></span><span></span><span></span></div></div>
      <div class="slider-ring"></div>
    </div>
  </section>

  <section class="month" style="top:265px">
    <div class="year">2025</div>
    <div class="week-label">Woche<br>Week<br>Semaine</div>
    <div class="title">JANUAR . JANUARY . JANVIER</div>
    <div class="weekdays">
      <span>Montag<br>Monday<br>Lundi</span><span>Dienstag<br>Tuesday<br>Mardi</span><span>Mittwoch<br>Wednesday<br>Mercredi</span><span>Donnerstag<br>Thursday<br>Jeudi</span><span>Freitag<br>Friday<br>Vendredi</span><span>Samstag<br>Saturday<br>Samedi</span><span>Sonntag<br>Sunday<br>Dimanche</span>
    </div>
    <div class="band" style="top:57px">
      <div class="row"><div class="week">1</div><div class="days"><span></span><span></span><span>1</span><span>2</span><span>3</span><span>4</span><span class="sun">5</span></div></div>
      <div class="row"><div class="week">2</div><div class="days"><span>6</span><span>7</span><span>8</span><span>9</span><span>10</span><span>11</span><span class="sun">12</span></div></div>
      <div class="row"><div class="week">3</div><div class="days"><span>13</span><span>14</span><span>15</span><span>16</span><span>17</span><span>18</span><span class="sun">19</span></div></div>
      <div class="row"><div class="week">4</div><div class="days"><span>20</span><span>21</span><span>22</span><span>23</span><span>24</span><span>25</span><span class="sun">26</span></div></div>
      <div class="row"><div class="week">5</div><div class="days"><span>27</span><span>28</span><span>29</span><span>30</span><span>31</span><span></span><span></span></div></div>
    </div>
  </section>

  <section class="month" style="top:484px">
    <div class="year">2025</div>
    <div class="week-label">Woche<br>Week<br>Semaine</div>
    <div class="title">FEBRUAR . FEBRUARY . FÉVRIER</div>
    <div class="weekdays">
      <span>Montag<br>Monday<br>Lundi</span><span>Dienstag<br>Tuesday<br>Mardi</span><span>Mittwoch<br>Wednesday<br>Mercredi</span><span>Donnerstag<br>Thursday<br>Jeudi</span><span>Freitag<br>Friday<br>Vendredi</span><span>Samstag<br>Saturday<br>Samedi</span><span>Sonntag<br>Sunday<br>Dimanche</span>
    </div>
    <div class="band" style="top:55px">
      <div class="row"><div class="week">5</div><div class="days"><span></span><span></span><span></span><span></span><span></span><span>1</span><span class="sun">2</span></div></div>
      <div class="row"><div class="week">6</div><div class="days"><span>3</span><span>4</span><span>5</span><span>6</span><span>7</span><span>8</span><span class="sun">9</span></div></div>
      <div class="row"><div class="week">7</div><div class="days"><span>10</span><span>11</span><span>12</span><span>13</span><span>14</span><span>15</span><span class="sun">16</span></div></div>
      <div class="row"><div class="week">8</div><div class="days"><span>17</span><span>18</span><span>19</span><span>20</span><span>21</span><span>22</span><span class="sun">23</span></div></div>
      <div class="row"><div class="week">9</div><div class="days"><span>24</span><span>25</span><span>26</span><span>27</span><span>28</span><span></span><span></span></div></div>
    </div>
  </section>

  <div class="holiday-label">Feiertage<br>Holidays<br>Jours fériés</div>
  <div class="holidays de">
    <span class="name">Neujahrstag</span><span class="date">Jan 01</span>
    <span class="name">Offenbarung (BW, BY &amp; ST)</span><span class="date">Jan 06</span>
    <span class="name">Weihnachtsfeiertag</span><span class="date">Dez 25</span>
    <span class="name">Weihnachtsfeiertage</span><span class="date">Dez 26</span>
  </div>
  <div class="holidays en">
    <span class="name">New Year's Day</span><span class="date">01 January</span>
    <span class="name">Epiphany</span><span class="date">06 January</span>
    <span class="name">Immaculate Conception</span><span class="date">08 December</span>
    <span class="name">Christmas Eve</span><span class="date">24 December</span>
    <span class="name">Christmas Day</span><span class="date">25 December</span>
    <span class="name">Boxing Day</span><span class="date">26 December</span>
    <span class="name">New Year</span><span class="date">31 December</span>
  </div>
  <div class="holidays fr">
    <span class="name">Jour de l'An</span><span class="date">janv-01</span>
    <span class="name">Noël</span><span class="date">déc-25</span>
    <span class="name">Saint-Étienne</span><span class="date">déc-26</span>
  </div>
</div>

</body>
</html>
```